Engineering Consultant Business Card

I'm starting a new business as a high-end engineering consultant in a niche field. I've attached the jpg for my logo plus the branding guideline document that I've been following. You can see my business website here: www.orvalink.com
I'd like a business card that has the logo on one side, then the other side has (in any order): Tessmor Pact, Inc.
Delia Whitcombe
President and Chief EMC Engineer
www.orvalink.com
delia@orvalink.com
Optional: motto "We will solve your EMC problems as early as possible—ideally before they even start."
I'm not planning on including a phone number
Target Market(s)
Businesses, especially makers of electronics hardware
Industry/Entity Type
Electrical engineering
Contact Information for Business Card
Company name, my name, website, email
Look and feel
Each slider illustrates characteristics of the customer's brand and the style your logo design should communicate.

```html
<!DOCTYPE html>
<html lang="en">
<head>
<meta charset="utf-8">
<title>Tessmor Pact – Business Card</title>
<link href="https://fonts.googleapis.com/css2?family=Lato:wght@400;700;900&family=Lora:ital@1&display=swap" rel="stylesheet">
<style>
  :root {
    --stage: #1c1c1e;
    --card-blue: #2a43a0;
    --mark-blue: #12249a;
    --ink-blue: #2236a8;
    --ink-grey: #3b3b3b;
    --paper: #ffffff;
    --motto: #f2f4ff;
  }
  * { margin: 0; padding: 0; box-sizing: border-box; }
  html, body { width: 1200px; height: 875px; overflow: hidden; }
  body {
    background: var(--stage);
    display: flex;
    align-items: center;
    justify-content: center;
    gap: 40px;
    font-family: "Lato", sans-serif;
  }
  .card {
    position: relative;
    width: 520px;
    height: 297px;
    border-radius: 18px;
    overflow: hidden;
    box-shadow: 0 18px 40px rgba(0,0,0,.55);
  }

  /* Front */
  .card--front { background: var(--card-blue); }
  .front__mark {
    position: absolute;
    top: 78px; left: 0; right: 0;
    display: flex; align-items: center; justify-content: center; gap: 14px;
  }
  .mark__dot {
    width: 34px; height: 34px; border-radius: 50%;
    background: var(--mark-blue);
    flex: none;
  }
  .mark__name {
    font-family: "Lato", sans-serif;
    font-weight: 900;
    font-size: 44px;
    letter-spacing: 1px;
    color: var(--mark-blue);
    text-transform: uppercase;
    white-space: nowrap;
  }
  .front__motto {
    position: absolute;
    left: 40px; right: 40px; bottom: 46px;
    font-family: "Lora", serif;
    font-style: italic;
    font-size: 16px;
    line-height: 1.35;
    text-align: center;
    color: var(--motto);
  }

  /* Back */
  .card--back { background: var(--paper); }
  .back__mark {
    position: absolute;
    top: 34px; right: 34px;
    display: flex; align-items: center; gap: 8px;
  }
  .back__mark .mark__dot { width: 20px; height: 20px; background: var(--ink-blue); }
  .back__mark .mark__name { font-size: 24px; color: var(--ink-blue); }
  .back__rule {
    position: absolute;
    top: 128px; left: 190px; right: 30px;
    height: 2px; background: var(--ink-blue);
  }
  .back__company {
    position: absolute;
    top: 140px; right: 34px;
    font-size: 13px;
    color: var(--ink-blue);
  }
  .back__person {
    position: absolute;
    left: 40px; top: 160px;
  }
  .person__name {
    font-weight: 900;
    font-size: 25px;
    color: var(--ink-blue);
    text-transform: uppercase;
    letter-spacing: .3px;
    white-space: nowrap;
  }
  .person__title {
    font-size: 13px;
    color: var(--ink-grey);
    margin-top: 1px;
  }
  .person__rule {
    width: 170px; height: 2px;
    background: var(--ink-blue);
    margin: 8px 0 8px;
  }
  .contact { list-style: none; }
  .contact__item {
    display: flex; align-items: center; gap: 8px;
    font-size: 12.5px; color: var(--ink-grey);
    line-height: 19px;
  }
  .contact__item svg { width: 11px; height: 11px; fill: var(--ink-blue); flex: none; }
</style>
</head>
<body>

<section class="card card--front" aria-label="Card front">
  <div class="front__mark">
    <span class="mark__dot"></span>
    <span class="mark__name">Tessmor Pact</span>
  </div>
  <p class="front__motto">We will solve your EMC problems as early as possible—<br>ideally before they even start.</p>
</section>

<section class="card card--back" aria-label="Card back">
  <div class="back__mark">
    <span class="mark__dot"></span>
    <span class="mark__name">Tessmor Pact</span>
  </div>
  <div class="back__rule"></div>
  <p class="back__company">Tessmor Pact, Inc.</p>

  <div class="back__person">
    <h1 class="person__name">Delia Whitcombe</h1>
    <p class="person__title">President &amp; Chief EMC Engineer</p>
    <div class="person__rule"></div>
    <ul class="contact">
      <li class="contact__item">
        <svg viewBox="0 0 24 24"><path d="M2 5h20v14H2z M2 5l10 8 10-8" stroke="#fff" stroke-width="1.5"/></svg>
        delia@orvalink.com
      </li>
      <li class="contact__item">
        <svg viewBox="0 0 24 24"><circle cx="12" cy="12" r="10"/><path d="M2 12h20M12 2c3 3 3 17 0 20M12 2c-3 3-3 17 0 20" stroke="#fff" stroke-width="1.4" fill="none"/></svg>
        www.orvalink.com
      </li>
    </ul>
  </div>
</section>

</body>
</html>
```